Fahrzeugbeschriftung für Schreinerei
Es hat alles gut funktioniert. Wir hatten zwar auf englisch kommunizieren müssen, aber dank google-Übersetzter war das kein Problem. Die Vorschläge des Designers hatten mir alle, sofort gefallen. Thank you
Zielgruppe
Wir sind eine kleine Schreinerei. Unser Hauptgeschäft/ Spezialität sind hochwertige Massivholztreppen.
Natürlich zählen dazu auch Geländerbau und Treppenstufen.
Als Schreinerwerkstatt kümmern wir uns natürlich auch um Innenausbau, Türen, Möbel und Sonderanfertigungen.
Wir sind bekannt für perfekte Auftragsabwicklung, Kompetenz, perfekte Produkte, saubere, zügige Montage und Termintreue.
Zielgruppe sind hauptsächlich private Bauherren und Renovierer (eher individuelle Klasse statt Masse).
Aufgabenstellung
Treppen als Hauptprodukt/ Kerngeschäft das soll man gut erkennen können.
Schön wäre ein Slogan. Holzstruktur wäre vielleicht gut.
Die Schriftfarbe Orange haben wir seit 20 Jahren, ist aber nicht zwingend.
Beschriftet werden soll aktuell ein neuer Velmont Kargo, weiß, L2H2, Seiten geschlossen, Türen hinten verglast.
Das Design soll sich später auf Briefpapier, Visitenkarte,... wiederfinden.

```html
<!DOCTYPE html>
<html lang="de">
<head>
<meta charset="utf-8">
<title>Tischlermeister Wellbrink – Fahrzeugbeschriftung</title>
<link href="https://fonts.googleapis.com/css2?family=Open+Sans:wght@600;700;800&display=swap" rel="stylesheet">
<style>
  :root {
    --bg: #f4f4f4;
    --ink: #5b3b27;
    --ink-dark: #3f2818;
    --rule: #8d8d8d;
    --wood-light: #ecdccb;
    --wood-mid: #c9a789;
    --dot: #9a9a9a;
  }
  * { margin: 0; padding: 0; box-sizing: border-box; }
  html, body { width: 1200px; height: 600px; overflow: hidden; background: var(--bg); }
  body { font-family: "Open Sans", Arial, sans-serif; color: var(--ink); }

  .lettering { position: relative; width: 1200px; height: 600px; }
  .stair-visual, .frame-lines { position: absolute; left: 0; top: 0; }

  .text { position: absolute; white-space: nowrap; font-weight: 800; line-height: 1; }

  .trade-title { left: 160px; top: 58px; font-size: 40px; font-weight: 700; color: var(--ink-dark); letter-spacing: 0.5px; }

  .company-name { left: 636px; top: 46px; display: flex; align-items: baseline; gap: 14px; color: var(--ink-dark); }
  .company-name .first { font-size: 30px; font-weight: 700; color: var(--ink); }
  .company-name .last { font-size: 58px; font-weight: 800; }

  .trade-main { left: 220px; top: 166px; font-size: 52px; }
  .trade-amp { left: 262px; top: 240px; font-size: 20px; font-weight: 700; }
  .trade-sub { left: 162px; top: 292px; font-size: 52px; }

  .services { position: absolute; left: 672px; top: 164px; list-style: none; }
  .services li { position: relative; font-size: 29px; font-weight: 700; line-height: 40px; padding-left: 22px; }
  .services li::before { content: ""; position: absolute; left: 0; top: 17px; width: 8px; height: 8px; border-radius: 50%; background: var(--dot); }
  .services li:first-child::before { display: none; }

  .slogan { left: 150px; top: 392px; font-size: 36px; }
  .website { left: 196px; top: 534px; font-size: 26px; font-weight: 700; color: var(--ink-dark); }
</style>
</head>
<body>
<main class="lettering">
  <svg class="stair-visual" width="1200" height="600" viewBox="0 0 1200 600" role="img" aria-label="Illustration einer Massivholztreppe mit Geländer">
    <defs>
      <linearGradient id="wood" x1="0" y1="1" x2="1" y2="0">
        <stop offset="0" stop-color="#c9a789"/>
        <stop offset="1" stop-color="#ecdccb"/>
      </linearGradient>
    </defs>
    <polygon points="375,560 470,560 700,40 610,40" fill="url(#wood)" opacity="0.85"/>
  </svg>

  <svg class="frame-lines" width="1200" height="600" viewBox="0 0 1200 600" aria-hidden="true">
    <g fill="none" stroke="#8d8d8d" stroke-width="2">
      <line x1="135" y1="20" x2="1085" y2="20"/>
      <line x1="135" y1="20" x2="135" y2="142"/>
      <line x1="1085" y1="20" x2="1085" y2="142"/>
      <line x1="608" y1="30" x2="608" y2="132"/>
      <line x1="135" y1="142" x2="1085" y2="142"/>
      <path d="M135 142 V360 Q135 370 145 370 H1085 V142"/>
      <line x1="135" y1="460" x2="1085" y2="460"/>
    </g>
  </svg>

  <div class="text trade-title">Tischlermeister</div>
  <div class="text company-name"><span class="first">Konrad</span><span class="last">Wellbrink</span></div>

  <div class="text trade-main">Treppen</div>
  <div class="text trade-amp">&amp;</div>
  <div class="text trade-sub">Tischlerbetrieb</div>

  <ul class="services">
    <li>Treppen</li>
    <li>Innenausbau</li>
    <li>Türen &amp; Möbel</li>
    <li>Sonderanfertigungen</li>
  </ul>

  <div class="text slogan">Massivholz mit Charakter – Stufe für Stufe</div>
  <div class="text website">www.treppen-wellbrink.de</div>
</main>
</body>
</html>
```